[WEB DESIGN - Start-up] Online LOANS against Luxury Assets - Needs a Web Design

Hello,
We need a web design for a new company. We make online LOANS against Luxury assets.
The name is private, that's why you could remplace it by the term "LOGO" or "ENTERPRISE".

In attachments, you'll find few models that we would like. Nonetheless, we don't want a copy of these screenshots. They are only prototypes that we made. Here we expect you to lead a professional web Design with your intuition and your ideas.

The final design should communicate start-up spirit, professionalism and fluidity.

Best Regards.

Industry/Entity Type

Finance

Number of Pages Required

2 page

Font styles to use
Sans Serif

Colors
f78f20
ffffff
b2b2b2
e9e9e9

Requirements
Must have
• The designer will draw on the 2015 web trends.
• The subject site is serious (loans against luxury assets), but the site should be modern and pleasant.
• PLEASE REFER YOU TO MY MODEL ( ATTACHMENTS)
Nice to have
• Surprise-me ! Welcome to a lot of imagination.

```html
<!DOCTYPE html>
<html lang="fr">
<head>
<meta charset="utf-8">
<title>Orvane — Prêts sur biens de luxe</title>
<link rel="stylesheet" href="https://fonts.googleapis.com/css2?family=Oswald:wght@400;500;700&family=Open+Sans:wght@400;600;700&display=swap">
<style>
:root{
  --orange:#f78f20;
  --white:#ffffff;
  --grey:#b2b2b2;
  --light:#e9e9e9;
  --dark:#2b2b2b;
  --darker:#1e1e1e;
  --text:#555555;
}
*{box-sizing:border-box;margin:0;padding:0}
html,body{width:1200px;height:2868px;overflow:hidden}
body{font-family:"Open Sans",Arial,sans-serif;color:var(--text);background:var(--white);font-size:13px}
h1,h2,h3,.nav,.step-label,.counter{font-family:"Oswald","Arial Narrow",sans-serif}

/* header & hero */
.hero{position:relative;height:660px;background:linear-gradient(135deg,#6d7680 0%,#9aa2aa 30%,#4b4f55 55%,#b56a28 75%,#2a2c30 100%)}
.hero-photo{position:absolute;inset:0}
.topbar{position:absolute;top:0;left:0;right:0;height:72px;background:rgba(20,20,20,.55);display:flex;align-items:center;padding:0 60px;justify-content:space-between}
.brand{font-family:"Oswald",sans-serif;font-weight:700;font-size:38px;color:var(--white);letter-spacing:1px}
.nav{display:flex;gap:30px;font-size:14px;color:var(--white);letter-spacing:.5px}
.nav .active{color:var(--orange)}
.hero-side-arrow{position:absolute;top:305px;width:22px;height:40px;background:rgba(0,0,0,.4)}
.quote-form{position:absolute;left:120px;top:100px;width:230px;background:rgba(40,40,40,.8);padding:18px}
.quote-form h3{color:var(--white);font-weight:500;font-size:20px;margin-bottom:14px}
.field{height:30px;background:var(--white);margin-bottom:10px;font-size:11px;color:#999;padding:7px 10px;display:flex;gap:8px;align-items:center}
.field i{width:10px;height:10px;background:var(--grey);display:inline-block}
.btn{display:inline-block;background:var(--orange);color:var(--white);font-size:11px;font-weight:700;padding:9px 18px;margin-top:6px}
.hero-title{position:absolute;left:120px;top:478px;color:var(--white);font-size:46px;line-height:52px;font-weight:700;text-transform:uppercase}

/* steps */
.steps{height:240px;background:var(--white);position:relative;padding:50px 120px 0}
.steps-line{position:absolute;top:86px;left:170px;right:170px;height:2px;background:var(--orange)}
.steps-row{display:flex;justify-content:space-between;position:relative}
.step{width:210px}
.step-label{display:inline-block;background:var(--orange);color:var(--white);padding:6px 12px;line-height:1.1}
.step-label small{display:block;font-size:10px;font-weight:400}
.step-label strong{font-size:22px;font-weight:500}
.step p{font-size:11px;line-height:16px;margin-top:14px;color:#888}

/* assets */
.assets{height:640px;background:var(--light);padding-top:46px;position:relative}
.section-title{text-align:center;font-size:24px;font-weight:500;color:#333;text-transform:uppercase}
.grid{width:840px;margin:34px auto 0;display:grid;grid-template-columns:repeat(5,1fr);gap:8px}
.tile{height:170px;position:relative;overflow:hidden}
.tile span{position:absolute;left:0;right:0;bottom:0;background:rgba(255,255,255,.9);font-size:12px;text-align:center;padding:6px 0;color:#333}
.arrow{position:absolute;top:1230px}
.t1{background:linear-gradient(135deg,#f0a040,#c8681a)}
.t2{background:linear-gradient(135deg,#444,#999)}
.t3{background:linear-gradient(135deg,#3a2a22,#a0704a)}
.t4{background:linear-gradient(135deg,#f2f2f2,#cfcfcf)}
.t5{background:linear-gradient(135deg,#d9c9a8,#8c7a5c)}
.t6{background:linear-gradient(135deg,#1e2630,#6a7480)}
.t7{background:linear-gradient(135deg,#e07820,#5a3a20)}
.t8{background:linear-gradient(135deg,#a8703a,#5a3418)}
.t9{background:linear-gradient(135deg,#333,#b0b0b0)}
.t10{background:linear-gradient(135deg,#eee,#c4c4c4)}
.t11{background:linear-gradient(135deg,#5a4a3a,#c09a6a)}
.t12{background:linear-gradient(135deg,#1a1a1a,#8a6a50)}
.t13{background:linear-gradient(135deg,#0f2740,#3f86b8)}
.t14{background:linear-gradient(135deg,#c89a50,#5a4020)}
.t15{background:linear-gradient(135deg,#f4f4f4,#d4d4d4)}

/* help */
.help{height:480px;padding-top:58px;background:var(--white)}
.help .section-title{color:var(--orange)}
.help-row{width:840px;margin:48px auto 0;display:flex;gap:30px}
.help-card{flex:1;height:230px;border:1px solid var(--light);text-align:center;padding-top:30px}
.help-card svg{display:block;margin:0 auto 22px}
.help-card p{font-size:12px;color:#999}
.help-card strong{display:block;color:var(--orange);font-size:14px;margin-top:4px;font-weight:600}

/* proof */
.proof{height:720px;background:var(--light);padding-top:64px}
.proof .section-title{font-size:22px}
.proof-cols{width:960px;margin:44px auto 0;display:flex;gap:40px}
.proof-col{flex:1}
.proof-col h3{color:var(--orange);font-size:18px;font-weight:500;margin-bottom:16px}
.quote{background:var(--white);padding:18px;font-size:11px;line-height:17px;color:#888;margin-bottom:16px}
.quote-author{display:flex;align-items:center;gap:12px;margin:0 0 30px 10px;font-size:11px}
.avatar{width:44px;height:44px;border-radius:50%;background:var(--grey)}
.counter{display:flex;gap:4px;margin-bottom:16px}
.counter b{width:44px;height:60px;background:var(--darker);color:var(--white);font-size:40px;font-weight:500;text-align:center;line-height:60px}
.counter b.gap{background:transparent;width:10px}
.fact{font-size:11px;line-height:17px;color:#888;margin-bottom:40px}

/* footer */
.footer{height:128px;background:var(--dark);color:#aaa;display:flex;padding:18px 120px;gap:40px;font-size:10px;line-height:14px}
.footer h3{color:var(--white);font-size:16px;font-weight:500;margin-bottom:6px}
.footer .about{width:560px}
.footer ul{list-style:none}
</style>
</head>
<body>

<header class="hero">
  <div class="hero-photo" role="img" aria-label="Berline de luxe garée au crépuscule"></div>
  <div class="topbar">
    <div class="brand">ORVANE</div>
    <nav class="nav">
      <span class="active">CONCEPT</span><span>LES BIENS</span><span>ESTIMATION</span><span>FAQ</span><span>MON COMPTE</span><span>CALL : 01 00 00 00 00</span>
    </nav>
  </div>
  <div class="hero-side-arrow" style="left:0"></div>
  <div class="hero-side-arrow" style="right:0"></div>
  <form class="quote-form">
    <h3>Natures de l'objet</h3>
    <div class="field"><i></i>Sélectionnez</div>
    <div class="field"><i></i>Valeur estimée</div>
    <div class="field"><i></i>Votre email</div>
    <span class="btn">ESTIMER MON BIEN</span>
  </form>
  <h1 class="hero-title">On se lasse de tout,<br>sauf de l'argent</h1>
</header>

<section class="steps">
  <div class="steps-line"></div>
  <div class="steps-row">
    <div class="step"><div class="step-label"><small>ÉTAPE 1</small><strong>ESTIMATION</strong></div><p>Décrivez votre bien en ligne et recevez une première estimation gratuite sous vingt-quatre heures, sans engagement de votre part.</p></div>
    <div class="step"><div class="step-label"><small>ÉTAPE 2</small><strong>PAIEMENT</strong></div><p>Après expertise, nous vous versons le montant du prêt par virement rapide, en toute simplicité et sans frais cachés.</p></div>
    <div class="step"><div class="step-label"><small>ÉTAPE 3</small><strong>SÉCURISATION</strong></div><p>Votre bien est conservé dans un coffre assuré et surveillé, pendant toute la durée de votre prêt.</p></div>
    <div class="step"><div class="step-label"><small>ÉTAPE 4</small><strong>RACHAT</strong></div><p>Remboursez votre prêt à votre rythme et récupérez votre bien à tout moment, en parfait état.</p></div>
  </div>
</section>

<section class="assets">
  <h2 class="section-title">Les biens que nous acceptons</h2>
  <div class="grid">
    <div class="tile t1" role="img" aria-label="Tableau abstrait orange"><span>Art Tableaux</span></div>
    <div class="tile t2" role="img" aria-label="Pierres précieuses"><span>Pierres Précieuses</span></div>
    <div class="tile t3" role="img" aria-label="Bouteilles de vin"><span>Vins &amp; Spiritueux</span></div>
    <div class="tile t4" role="img" aria-label="Objet d'art décoratif"><span>Art Décoratif</span></div>
    <div class="tile t5" role="img" aria-label="Sculpture contemporaine"><span>Art Contemporain</span></div>
    <div class="tile t6" role="img" aria-label="Montre de luxe"><span>Montres</span></div>
    <div class="tile t7" role="img" aria-label="Voiture de sport"><span>Véhicules</span></div>
    <div class="tile t8" role="img" aria-label="Pièces d'or"><span>Métaux Précieux</span></div>
    <div class="tile t9" role="img" aria-label="Sac en cuir"><span>Maroquinerie</span></div>
    <div class="tile t10" role="img" aria-label="Objet de collection"><span>Collections</span></div>
    <div class="tile t11" role="img" aria-label="Instrument de musique"><span>Instruments</span></div>
    <div class="tile t12" role="img" aria-label="Bijoux portés"><span>Bijoux</span></div>
    <div class="tile t13" role="img" aria-label="Objectif photo"><span>High-Technology Equipments</span></div>
    <div class="tile t14" role="img" aria-label="Statue ancienne"><span>Antiquités</span></div>
    <div class="tile t15" role="img" aria-label="Mobilier design"><span>Mobilier</span></div>
  </div>
  <svg class="arrow" style="left:150px;top:330px" width="14" height="24" viewBox="0 0 14 24"><path d="M12 2 2 12l10 10" fill="none" stroke="#888" stroke-width="3"/></svg>
  <svg class="arrow" style="right:150px;top:330px" width="14" height="24" viewBox="0 0 14 24"><path d="M2 2l10 10-10 10" fill="none" stroke="#888" stroke-width="3"/></svg>
</section>

<section class="help">
  <h2 class="section-title">Besoin d'aide ? Nous sommes à votre écoute</h2>
  <div class="help-row">
    <div class="help-card">
      <svg width="80" height="80" viewBox="0 0 80 80"><circle cx="40" cy="40" r="38" fill="none" stroke="#b2b2b2" stroke-width="2"/><path d="M30 27c3-2 5 0 6 3l1 4-3 3c2 4 5 7 9 9l3-3 4 1c3 1 5 3 3 6-2 3-5 4-9 2-8-4-13-9-16-17-1-4 0-6 2-8z" fill="#b2b2b2"/></svg>
      <p>Nous vous répondons au</p><strong>01 00 00 00 00</strong>
    </div>
    <div class="help-card">
      <svg width="80" height="80" viewBox="0 0 80 80"><circle cx="40" cy="40" r="38" fill="none" stroke="#b2b2b2" stroke-width="2"/><text x="40" y="52" text-anchor="middle" font-family="Oswald,sans-serif" font-size="36" fill="#b2b2b2">?</text></svg>
      <p>Toutes vos réponses dans nos</p><strong>Questions Fréquentes</strong>
    </div>
    <div class="help-card">
      <svg width="80" height="80" viewBox="0 0 80 80"><circle cx="40" cy="40" r="38" fill="none" stroke="#b2b2b2" stroke-width="2"/><rect x="24" y="29" width="32" height="22" fill="none" stroke="#b2b2b2" stroke-width="2"/><path d="M24 29l16 12 16-12" fill="none" stroke="#b2b2b2" stroke-width="2"/></svg>
      <p>Écrivez-nous via le</p><strong>Formulaire de contact</strong><p>contact@orvane-exemple.fr</p>
    </div>
  </div>
</section>

<section class="proof">
  <h2 class="section-title">Entreprise est nº1 de la vente avec faculté de rachat</h2>
  <div class="proof-cols">
    <div class="proof-col">
      <h3>Derniers Témoignages</h3>
      <div class="quote">« Service rapide et très professionnel. J'ai obtenu mon prêt en deux jours et récupéré ma montre sans aucune difficulté. Je recommande vivement cette équipe attentive. »</div>
      <div class="quote-author"><div class="avatar" role="img" aria-label="Photo du client"></div><div><strong>Marc D.</strong><br>Client depuis 2014</div></div>
      <div class="quote">« Une solution idéale pour financer mon projet sans vendre mes bijoux de famille. Estimation juste, conseillers disponibles et paiement immédiat. »</div>
      <div class="quote-author"><div class="avatar" role="img" aria-label="Photo de la cliente"></div><div><strong>Claire L.</strong><br>Cliente depuis 2015</div></div>
    </div>
    <div class="proof-col">
      <h3>Quelques Chiffres</h3>
      <div class="counter"><b>0</b><b>5</b><b>5</b><b>3</b><b class="gap"></b><b>1</b><b>9</b></div>
      <p class="fact">Biens de luxe confiés à nos experts depuis la création de l'entreprise. Chaque objet est expertisé, assuré et conservé dans un coffre sécurisé jusqu'à son rachat par son propriétaire.</p>
      <div class="counter"><b>0</b><b>4</b><b>8</b><b class="gap"></b><b>0</b><b>8</b></div>
      <p class="fact">Clients satisfaits ayant récupéré leur bien après remboursement. Notre taux de rachat témoigne de la confiance accordée à notre service.</p>
    </div>
  </div>
</section>

<footer class="footer">
  <div class="about">
    <h3>Vendre en vue de racheter</h3>
    <p>La vente avec faculté de rachat vous permet d'obtenir rapidement des liquidités en confiant un bien de valeur, puis de le récupérer à l'issue du contrat. Une solution souple, confidentielle et sans conditions de revenus.</p>
  </div>
  <ul><li>Accueil</li><li>Concept</li><li>Les biens</li><li>Estimation</li><li>FAQ</li></ul>
  <ul><li>Mon compte</li><li>Contact</li><li>Mentions légales</li><li>CGV</li></ul>
  <div><p>ORVANE<br>12 rue de l'Exemple<br>75000 Paris<br><br>Copyright © 2015 ORVANE. Tous droits réservés.</p></div>
</footer>

</body>
</html>
```